To design a brand identity that is simple and creative with 'Valdor' as the brand name, I like modern simple fonts like helvetica neue, I want to print both sides of the card, I am open to dark front and white back, but the design needs to transfer well to letter heads and email signatures, I am looking for sophisticated and elegant, but open minded about clever and off the wall, I do not do 'boring' Valdor Holdings is the mother company for a small group, specialising in Management & consulting, Software development and construction, we have a high level of integrity, we are transparent and accountable for what we do. my images are provided as a guide only, Im not expecting them to be just copied, Im looking for a creator and passionate thinker, who will put life into their work.

Target Market(s)

usually business minded people who are looking for something different in me, such as leadership, confidence and focus with thinking that is per haps a little outside the box..

Industry/Entity Type

Construction

Requirements
Must have
• clean, minmalistic
Nice to have
• custom logo
Should not have
• boring, traditional

```html
<!DOCTYPE html>
<html lang="en">
<head>
<meta charset="utf-8">
<title>Valdor Holdings – Business Card</title>
<link href="https://fonts.googleapis.com/css2?family=Quicksand:wght@400;500&display=swap" rel="stylesheet">
<style>
  :root {
    --stage: #c3c3c3;
    --card: #ffffff;
    --accent-orange: #e0632a;
    --tagline-grey: #7a7a7a;
    --ink: #262626;
    --paper-white: #ffffff;
    --magenta: #e0147a;
    --red: #e3262a;
    --amber: #f5a20c;
    --yellow: #f7c300;
    --green: #0a9348;
    --slate: #6f7a72;
  }
  html, body {
    margin: 0;
    padding: 0;
    overflow: hidden;
    background: var(--stage);
  }
  .stage {
    position: relative;
    width: 1200px;
    height: 790px;
    background: var(--stage);
    overflow: hidden;
    font-family: "Quicksand", "Helvetica Neue", Arial, sans-serif;
  }
  .card {
    position: absolute;
    width: 458px;
    height: 272px;
  }
  .card-shape {
    position: absolute;
    left: 0;
    top: 0;
    width: 458px;
    height: 272px;
  }
  .card--front-top { left: 107px; top: 88px; }
  .card--front-bottom { left: 107px; top: 427px; }
  .card--back-top { left: 634px; top: 88px; }
  .card--back-bottom { left: 634px; top: 427px; }

  /* Front */
  .brand {
    position: absolute;
    left: 84px;
    top: 86px;
    height: 52px;
    display: flex;
    align-items: center;
    gap: 16px;
  }
  .brand-dot {
    width: 40px;
    height: 40px;
    border-radius: 50%;
    background: var(--accent-orange);
    flex: none;
  }
  .brand-name {
    margin: 0;
    font-weight: 500;
    font-size: 48px;
    line-height: 1;
    color: var(--ink);
    letter-spacing: 0.5px;
  }
  .tagline {
    position: absolute;
    right: 89px;
    top: 150px;
    margin: 0;
    font-size: 15px;
    font-weight: 400;
    line-height: 20px;
    color: var(--tagline-grey);
  }
  .services {
    position: absolute;
    left: 0;
    top: 174px;
    width: 458px;
    text-align: center;
    margin: 0;
    font-size: 12.5px;
    font-weight: 500;
    line-height: 16px;
    color: var(--ink);
  }
  .services .sep { color: var(--accent-orange); padding: 0 3px; }

  /* Back */
  .contact {
    position: absolute;
    left: 0;
    top: 0;
    width: 458px;
    height: 272px;
    text-align: center;
    color: var(--ink);
  }
  .card--back-bottom .contact { color: var(--paper-white); }
  .contact p {
    position: absolute;
    left: 0;
    width: 100%;
    margin: 0;
    font-weight: 500;
  }
  .contact-email { top: 83px; font-size: 18px; line-height: 24px; }
  .contact-role { top: 109px; font-size: 12.5px; line-height: 16px; }
  .contact-phone { top: 148px; font-size: 14px; line-height: 18px; }
  .contact-address { top: 171px; font-size: 14px; line-height: 18px; }
  .contact-rule {
    position: absolute;
    top: 137px;
    left: 66px;
    width: 326px;
    height: 1px;
    background: var(--ink);
  }
  .card--back-bottom .contact-rule { background: var(--paper-white); }
</style>
</head>
<body>
<main class="stage">

  <section class="card card--front card--front-top">
    <svg class="card-shape" viewBox="0 0 458 272" aria-hidden="true">
      <circle cx="135" cy="136" r="135" fill="var(--card)"/>
      <circle cx="323" cy="136" r="135" fill="var(--card)"/>
    </svg>
    <div class="brand">
      <span class="brand-dot"></span>
      <h1 class="brand-name">Valdor</h1>
    </div>
    <p class="tagline">..built with clear intent.</p>
    <p class="services">management<span class="sep">•</span>software<span class="sep">•</span>construction</p>
  </section>

  <section class="card card--back card--back-top">
    <svg class="card-shape" viewBox="0 0 458 272" role="img" aria-label="Card back in a soft magenta, orange, yellow and green colour blend">
      <defs>
        <clipPath id="back-outline-a">
          <circle cx="135" cy="136" r="135"/>
          <circle cx="323" cy="136" r="135"/>
        </clipPath>
        <linearGradient id="back-blend-a" x1="0" y1="0" x2="1" y2="0">
          <stop offset="0" stop-color="var(--magenta)"/>
          <stop offset="0.25" stop-color="var(--red)"/>
          <stop offset="0.45" stop-color="var(--yellow)"/>
          <stop offset="0.6" stop-color="var(--amber)"/>
          <stop offset="0.8" stop-color="var(--green)"/>
          <stop offset="1" stop-color="var(--slate)"/>
        </linearGradient>
      </defs>
      <rect width="458" height="272" fill="url(#back-blend-a)" clip-path="url(#back-outline-a)"/>
    </svg>
    <div class="contact">
      <p class="contact-email">adrian@valdor.holdings</p>
      <p class="contact-role">client ambassador</p>
      <span class="contact-rule"></span>
      <p class="contact-phone">M. +61 0438 512 904</p>
      <p class="contact-address">PO BOX 418 Perth 6031</p>
    </div>
  </section>

  <section class="card card--front card--front-bottom">
    <svg class="card-shape" viewBox="0 0 458 272" aria-hidden="true">
      <circle cx="135" cy="136" r="135" fill="var(--card)"/>
      <circle cx="323" cy="136" r="135" fill="var(--card)"/>
    </svg>
    <div class="brand">
      <span class="brand-dot"></span>
      <h2 class="brand-name">Valdor</h2>
    </div>
    <p class="tagline">..built with clear intent.</p>
    <p class="services">management<span class="sep">•</span>software<span class="sep">•</span>construction</p>
  </section>

  <section class="card card--back card--back-bottom">
    <svg class="card-shape" viewBox="0 0 458 272" role="img" aria-label="Card back in a soft magenta, orange, yellow and green colour blend">
      <defs>
        <clipPath id="back-outline-b">
          <circle cx="135" cy="136" r="135"/>
          <circle cx="323" cy="136" r="135"/>
        </clipPath>
        <linearGradient id="back-blend-b" x1="0" y1="0" x2="1" y2="0">
          <stop offset="0" stop-color="var(--magenta)"/>
          <stop offset="0.25" stop-color="var(--red)"/>
          <stop offset="0.45" stop-color="var(--yellow)"/>
          <stop offset="0.6" stop-color="var(--amber)"/>
          <stop offset="0.8" stop-color="var(--green)"/>
          <stop offset="1" stop-color="var(--slate)"/>
        </linearGradient>
      </defs>
      <rect width="458" height="272" fill="url(#back-blend-b)" clip-path="url(#back-outline-b)"/>
    </svg>
    <div class="contact">
      <p class="contact-email">adrian@valdor.holdings</p>
      <p class="contact-role">client ambassador</p>
      <span class="contact-rule"></span>
      <p class="contact-phone">M. +61 0438 512 904</p>
      <p class="contact-address">PO BOX 418 Perth 6031</p>
    </div>
  </section>

</main>
</body>
</html>
```